Halvercott Orthodontics business card

Using our existing logo (created with ArtFolio), please create a tasteful, contemporary business card. We are father and daughter orthodontists specializing in braces, clarafit, etc to design healthy, beautiful smiles for children, adolescents, and adults. We would like the design to be family-friendly but not childish.
The final design should include all of the information without looking cluttered (I hope! If necessary to achieve an optimal design, please consider making the card double-sided)
Purple, black, silver on a white card
Please include the following information:
Halvercott Orthodontics (logo)
Marguerite L. Halvercott, DMD
Douglas R. Halvercott, DMD

312 Bramblewood Street
North Andover, MA 01899
978.555.0142

847C Quarry Hollow Street
Methuen, MA 01898
978.555.0187

email frontdesk@halvercottortho.example
website www.halvercottortho.example

```html
<!DOCTYPE html>
<html lang="en">
<head>
<meta charset="utf-8">
<title>Halvercott Orthodontics business card</title>
<link href="https://fonts.googleapis.com/css2?family=Roboto:wght@400;700&display=swap" rel="stylesheet">
<style>
  :root {
    --bg: #d9d9d9;
    --purple: #67308f;
    --grey: #858585;
    --grey-light: #929292;
    --white: #ffffff;
    --silver: #6f6f6f;
  }
  * { margin: 0; padding: 0; box-sizing: border-box; }
  html, body { width: 1200px; height: 711px; overflow: hidden; }
  body {
    background: var(--bg);
    font-family: "Roboto", sans-serif;
    position: relative;
  }
  .card {
    position: absolute;
    top: 76px;
    width: 320px;
    height: 560px;
    border-radius: 22px;
    overflow: hidden;
    box-shadow: 0 10px 24px rgba(0,0,0,.25);
  }
  .card-front { left: 250px; background: var(--purple); }
  .card-back { left: 630px; background: var(--white); }

  .front-brand {
    position: absolute;
    left: 50%; top: 50%;
    transform: translate(-50%, -50%) rotate(-90deg);
    display: flex; align-items: center; gap: 14px;
    white-space: nowrap;
    color: var(--white);
    font-weight: 400;
    font-size: 34px;
    letter-spacing: 1px;
  }
  .brand-dot {
    width: 34px; height: 34px; border-radius: 50%;
    background: var(--white);
  }

  .back-brand {
    position: absolute; top: 46px; left: 0; width: 100%;
    display: flex; justify-content: center; align-items: center; gap: 8px;
    color: var(--purple); font-size: 21px; font-weight: 400;
  }
  .back-brand .brand-dot { width: 18px; height: 18px; background: var(--purple); }

  .doctors {
    position: absolute; top: 128px; width: 100%;
    text-align: center; color: var(--purple);
    font-weight: 700; font-size: 16px; line-height: 1.35;
  }
  .back-band { position: absolute; left: 0; top: 0; width: 100%; height: 100%; }

  .offices {
    position: absolute; top: 258px; width: 100%;
    text-align: center; color: var(--white);
    font-size: 13px; line-height: 1.4;
  }
  .office + .office { margin-top: 18px; }
  .phone {
    color: var(--purple); font-size: 17px; font-weight: 400;
    display: inline-flex; align-items: center; gap: 6px;
  }
  .phone svg { width: 14px; height: 14px; }

  .online {
    position: absolute; bottom: 42px; left: 34px;
    color: var(--white); font-size: 13px; line-height: 1.9;
  }
  .online-row { display: flex; align-items: center; gap: 8px; }
  .online-row svg { width: 14px; height: 14px; flex: none; }
</style>
</head>
<body>
  <section class="card card-front" aria-label="Card front">
    <div class="front-brand"><span class="brand-dot"></span>Halvercott Orthodontics</div>
  </section>

  <section class="card card-back" aria-label="Card back">
    <svg class="back-band" viewBox="0 0 320 560" preserveAspectRatio="none" aria-hidden="true">
      <path d="M0 218 C90 238 160 230 200 190 C240 150 280 165 320 200 L320 560 L0 560 Z" fill="var(--grey)"/>
    </svg>

    <div class="back-brand"><span class="brand-dot"></span>Halvercott Orthodontics</div>

    <div class="doctors">
      <p>Marguerite L. Halvercott, DMD</p>
      <p>Douglas R. Halvercott, DMD</p>
    </div>

    <div class="offices">
      <div class="office">
        <p>312 Bramblewood Street</p>
        <p>North Andover, MA 01899</p>
        <p class="phone"><svg viewBox="0 0 24 24"><path fill="currentColor" d="M6.6 10.8a15 15 0 0 0 6.6 6.6l2.2-2.2a1 1 0 0 1 1-.25 11.4 11.4 0 0 0 3.6.57 1 1 0 0 1 1 1V20a1 1 0 0 1-1 1A17 17 0 0 1 3 4a1 1 0 0 1 1-1h3.5a1 1 0 0 1 1 1c0 1.25.2 2.45.57 3.57a1 1 0 0 1-.25 1z"/></svg>978.555.0142</p>
      </div>
      <div class="office">
        <p>847C Quarry Hollow Street</p>
        <p>Methuen, MA 01898</p>
        <p class="phone"><svg viewBox="0 0 24 24"><path fill="currentColor" d="M6.6 10.8a15 15 0 0 0 6.6 6.6l2.2-2.2a1 1 0 0 1 1-.25 11.4 11.4 0 0 0 3.6.57 1 1 0 0 1 1 1V20a1 1 0 0 1-1 1A17 17 0 0 1 3 4a1 1 0 0 1 1-1h3.5a1 1 0 0 1 1 1c0 1.25.2 2.45.57 3.57a1 1 0 0 1-.25 1z"/></svg>978.555.0187</p>
      </div>
    </div>

    <div class="online">
      <p class="online-row"><svg viewBox="0 0 24 24"><circle cx="12" cy="12" r="10" fill="var(--purple)"/><path d="M2 12h20M12 2c3 3 3 17 0 20M12 2c-3 3-3 17 0 20" stroke="#fff" stroke-width="1.2" fill="none"/></svg>www.halvercottortho.example</p>
      <p class="online-row"><svg viewBox="0 0 24 24"><rect x="2" y="5" width="20" height="14" rx="2" fill="var(--purple)"/><path d="M2 6l10 7 10-7" stroke="#fff" stroke-width="1.4" fill="none"/></svg>frontdesk@halvercottortho.example</p>
    </div>
  </section>
</body>
</html>
```